Stationery Design Project

We need a stationery design for a consultancy called 'Marlow Ridge'. The design should communicate innovation and professionalism. The colors used should complement our logo. Please include source files for winning design.

Requirements
Must have
• Logo with company name should be included. Font of the text in logo should not be altered. Paper should be A4 sized and not Letter sized.

```html
<!DOCTYPE html>
<html lang="en">
<head>
<meta charset="utf-8">
<title>Marlow Ridge — Business Card</title>
<link href="https://fonts.googleapis.com/css2?family=Cinzel:wght@400;600&family=PT+Serif:wght@700&family=Roboto:wght@400&display=swap" rel="stylesheet">
<style>
  :root {
    --canvas: #ece7df;
    --paper: #ffffff;
    --ink: #1a1a1a;
    --text-grey: #4a4a4a;
    --accent: #e08a2a;
    --sky-top: #ede3a8;
    --sky-mid: #e3b872;
    --sky-low: #d99558;
    --silhouette: #0d0d0d;
    --cream: #e8cf8e;
  }
  * { box-sizing: border-box; margin: 0; padding: 0; }
  html, body { width: 1200px; height: 1023px; overflow: hidden; }
  body { background: var(--canvas); position: relative; font-family: "Roboto", Arial, sans-serif; }

  .card {
    position: absolute;
    width: 580px;
    height: 330px;
    box-shadow: 0 10px 30px rgba(0,0,0,0.25);
    overflow: hidden;
  }

  /* Front */
  .card-front { left: 60px; top: 110px; background: var(--paper); }
  .card-front .bottom-band { position: absolute; left: 0; right: 0; bottom: 0; height: 30px; background: var(--ink); }

  .identity { position: absolute; right: 78px; top: 36px; text-align: right; }
  .identity .rule {
    position: absolute; left: calc(100% + 6px); top: 2px;
    width: 46px; height: 2px; background: var(--accent);
    transform-origin: left center; transform: rotate(-14deg);
  }
  .identity .person { font-family: "PT Serif", Georgia, serif; font-weight: 700; font-size: 24px; color: var(--accent); line-height: 1.1; }
  .identity .role { font-size: 18px; color: var(--text-grey); }

  .address { position: absolute; right: 40px; top: 122px; display: flex; gap: 8px; font-size: 13px; color: var(--text-grey); line-height: 1.35; }
  .address svg { margin-top: 2px; flex: none; }

  .brand { position: absolute; left: 36px; top: 118px; display: flex; align-items: center; gap: 12px; }
  .brand .dot { width: 58px; height: 58px; border-radius: 50%; background: var(--accent); }
  .brand .name { font-family: "Cinzel", Georgia, serif; font-size: 24px; color: var(--accent); }

  .contacts { position: absolute; left: 110px; top: 198px; list-style: none; font-size: 14px; color: var(--text-grey); line-height: 1.45; }
  .contacts li { display: flex; align-items: center; gap: 9px; }
  .contacts svg { flex: none; }

  /* Back */
  .card-back { left: 560px; top: 560px; }
  .card-back .scene {
    position: absolute; inset: 0;
    background: linear-gradient(170deg, var(--sky-top) 0%, var(--sky-mid) 55%, var(--sky-low) 100%);
  }
  .card-back .ground {
    position: absolute; right: 0; bottom: 0; width: 360px; height: 150px;
    background: var(--silhouette);
    clip-path: polygon(18% 15%, 50% 0, 100% 8%, 100% 100%, 0 100%);
  }
  .card-back .name { position: absolute; right: 30px; bottom: 26px; font-family: "Cinzel", Georgia, serif; font-size: 34px; color: var(--cream); white-space: nowrap; }
</style>
</head>
<body>
  <section class="card card-front">
    <div class="identity">
      <span class="rule"></span>
      <div class="person">Your Name</div>
      <div class="role">Director</div>
    </div>

    <div class="address">
      <svg width="12" height="12" viewBox="0 0 12 12" aria-hidden="true"><path d="M6 1 L11 5.5 H9.5 V11 H2.5 V5.5 H1 Z" fill="var(--accent)"/></svg>
      <div>21, Lorem ipsum,<br>Nunc eget sagittis<br>Proin ac viverra.</div>
    </div>

    <div class="brand">
      <span class="dot"></span>
      <span class="name">Marlow Ridge</span>
    </div>

    <ul class="contacts">
      <li><svg width="10" height="10" viewBox="0 0 10 10" aria-hidden="true"><path d="M2 1 L4 1 L4.5 3 L3.3 3.8 Q4.5 6 6.2 6.7 L7 5.5 L9 6 L9 8 Q5 9.5 1 2.5 Z" fill="var(--accent)"/></svg>555 0148 2731</li>
      <li><svg width="10" height="10" viewBox="0 0 10 10" aria-hidden="true"><rect x="2" y="0.5" width="6" height="9" rx="1" fill="var(--accent)"/></svg>555 0193 6604</li>
      <li><svg width="10" height="10" viewBox="0 0 10 10" aria-hidden="true"><rect x="0.5" y="2" width="9" height="6" fill="var(--accent)"/><path d="M0.5 2 L5 5.5 L9.5 2" stroke="#fff" fill="none"/></svg>info@marlowridge.com</li>
      <li><svg width="10" height="10" viewBox="0 0 10 10" aria-hidden="true"><circle cx="5" cy="5" r="4.5" fill="var(--accent)"/><path d="M0.5 5 H9.5 M5 0.5 V9.5" stroke="#fff" stroke-width="0.8"/></svg>www.marlowridge.com</li>
    </ul>

    <div class="bottom-band"></div>
  </section>

  <section class="card card-back">
    <div class="scene" role="img" aria-label="Silhouette of a lighthouse on a rocky shore under a warm sunset sky, with birds and rocks"></div>
    <div class="ground"></div>
    <div class="name">Marlow Ridge</div>
  </section>
</body>
</html>
```